会社で使用する封筒(角2、長3の2サイズ)のデザインをお願いします。

【カラーリング】
・別添の弊社ロゴマークに使用してある色(特に濃青)や白を基調とした色

【デザイン】
・なるべくシンプルなもので、目を引くような

【用途】
(角2)お客様への提案資料用、新卒採用 等
(長3)請求書等の書類のやりとり

※両サイズともデザインを統一して頂ければと思います。
会社名(株式会社 青葉総合企画)、ロゴマーク
デザイナーの皆様、ご提案ありがとうございます。
デザインについて追記させて頂きます。

封筒へは、弊社所在地の記載は不要です。
(移転があった場合にデザインの変更や刷り直しをなくすため)

また、弊社ロゴマークに使われている濃いめの青をもう少し出して
頂けるとありがたいです。
(グラデーションで段々と濃い→薄いという感じが理想です)

色々と注文して申し訳ありませんが、ご対応よろしくお願いします。

現在、弊社では封筒をはじめ、名刺や会社案内などの印刷物のデザインを刷新しようとしており、これまでのイメージを変えるシンプルながら斬新なデザインに魅力を感じました。封筒や名刺、提案資料のテンプレートなど様々な用途を考えた際に、一番使いやすくしっくり来た点が選択した一番の理由となります。

依頼した本人が、既製封筒への印刷なのかオーダーメイド封筒なのかを分かっていないまま依頼した事で、一部のデザイナー様にご迷惑をお掛けしたことをお詫びいたします。こんなにたくさんのご提案を頂き、正直選ぶのに大変苦労を致しました。本当にありがとうございました。

```html
<!DOCTYPE html>
<html lang="ja">
<head>
<meta charset="utf-8">
<title>角2封筒デザイン</title>
<link rel="stylesheet" href="https://fonts.googleapis.com/css2?family=Noto+Sans+JP:wght@400;700&family=Open+Sans:wght@600&display=swap">
<style>
  :root {
    --backdrop: #a8a9ab;
    --backdrop-shade: #8e8f91;
    --paper: #ffffff;
    --navy: #1f4a8f;
    --navy-deep: #1b3f7d;
    --lavender: #8e97c4;
    --ink: #1a1a1a;
    --label: #2b2b2b;
  }
  html, body {
    margin: 0;
    padding: 0;
    width: 1200px;
    height: 1200px;
    overflow: hidden;
    background: var(--backdrop);
  }
  .canvas {
    display: block;
    width: 1200px;
    height: 1200px;
  }
  .size-label {
    font-family: "Noto Sans JP", sans-serif;
    font-size: 18px;
    fill: var(--label);
  }
  .brand-name {
    font-family: "Noto Sans JP", sans-serif;
    font-weight: 700;
    font-size: 24px;
    fill: var(--ink);
  }
  .company-name {
    font-family: "Noto Sans JP", sans-serif;
    font-weight: 700;
    font-size: 13px;
    fill: var(--ink);
  }
  .tagline {
    font-family: "Open Sans", sans-serif;
    font-weight: 600;
    font-size: 41px;
    fill: var(--paper);
    letter-spacing: 0.5px;
  }
</style>
</head>
<body>
<svg class="canvas" viewBox="0 0 1200 1200" xmlns="http://www.w3.org/2000/svg">
  <defs>
    <linearGradient id="band-gradient" x1="480" y1="0" x2="942" y2="0" gradientUnits="userSpaceOnUse">
      <stop offset="0" stop-color="#ffffff" stop-opacity="0"/>
      <stop offset="0.12" stop-color="#e9ebf4"/>
      <stop offset="0.45" stop-color="var(--lavender)"/>
      <stop offset="0.75" stop-color="var(--navy)"/>
      <stop offset="1" stop-color="var(--navy-deep)"/>
    </linearGradient>
    <linearGradient id="shade-gradient" x1="0" y1="0" x2="1" y2="0">
      <stop offset="0" stop-color="#ffffff" stop-opacity="0"/>
      <stop offset="0.6" stop-color="#d6d8de"/>
      <stop offset="1" stop-color="#eceef2"/>
    </linearGradient>
  </defs>

  <text class="size-label" x="126" y="44">角2_D1</text>

  <!-- envelope -->
  <path class="envelope-shadow" d="M272,30 L956,30 L988,165 L988,1180 L246,1180 L246,160 Z" fill="var(--backdrop-shade)" opacity="0.55"/>
  <path class="envelope" d="M264,22 L948,22 L978,155 L978,1170 L236,1170 L236,150 Z" fill="var(--paper)"/>

  <!-- footer band -->
  <g class="footer-band">
    <path class="band-fill" d="M269,914 C430,985 560,1026 690,1020 C800,1014 880,962 942,924 L942,1140 L269,1140 Z" fill="url(#band-gradient)"/>
    <path class="band-shade" d="M700,1032 C800,1024 880,976 942,940 L942,952 C880,990 800,1034 700,1040 Z" fill="url(#shade-gradient)"/>
    <path class="band-line" d="M266,904 C430,980 560,1022 690,1016 C800,1010 880,958 942,920" fill="none" stroke="var(--navy)" stroke-width="4"/>
  </g>

  <!-- brand block -->
  <g class="brand">
    <text class="brand-name" x="282" y="1082">Aoba Planning</text>
    <text class="company-name" x="282" y="1126">株式会社 青葉総合企画</text>
  </g>

  <text class="tagline" x="584" y="1123">VALUE CREATOR</text>
</svg>
</body>
</html>
```